Dale Brannick - Senior Living Audio CDs - CD Design and Cover Design

I am an executive director in an assisted living facility. I have just started speaking, training, and coaching in the Senior Living Industry. I have 4 audio files that I want to put to a CD. The names of the CD's are:

1- Stewardship - Building Lasting Trust Inside Elder Care Homes
2- Why Every Retirement Home Exists Today
3- Captain's Compass - Where Focus Goes, Growth Flows
4- Team Hiring -Hidden Keys for Staff Loyalty

I think I can use the same CD cover for each CD. I just need the same design but 4 different ones with the names above. So everything will be the same but the name change. The inside cover will be I will consider other colors but it would be great if it would look good with the logo. I also need help with designing the CD face itself. I will be using a standard Jewel CD case. I need the front cover, the inside cover, and the back. The logo will be on all three.

On the front:

Part of me thinks it should be a clean simple design with my logo, my picture, and the title. But I am also curious about the picture of me with the elderly lady. - I need the 4 designs that are the same except the title.

On the Inside:

It can be the same design but the wording will be specific to that CD and the 4 insides will be:

All businesses rise and fall with leadership. This is especially true in the senior living industry. The life of that rise or fall is based on the culture the leader creates. Learn the 3 keys to what leaders know and do. Learn what the Importance Factor is and how you can put it to work to create and sustain a winning culture that will drive your business and occupancy above the rest.

What is Why Every Retirement Home Exists Today? Your understanding to the answer of this question makes all the difference. After you have gained this understanding it takes the right beliefs and behavior of associates to fulfill this purpose. What's the purpose? How is it fulfilled?

They want a captain not a boss. As a leader in senior living you steer the ship. What you put your attention on becomes the intention of your community. Your ability to create a vision, help people embrace that vision, and learn how to stay focused when the storms of the industry come raging, is the key to your success. There is a pattern to achieving this success. Come learn this pattern and how to apply it in your life and your business. It can make all the difference.

A business can not be better than it's people. The right people are the key not just people. Learn where your focus should be to hire the right people. After you hire then find out what you can do to retain them and engage them. If you want happy residents you need happy associates.

On the back it will need to have:

1- My Logo
2- www.DaleBrannick.com
3- Email: info@DaleBrannick.com
4- You could put the picture of me and the elderly lady as a watermark on the back with the above info.

I have a short turn around time and need designs quickly. I also need help with designing the CD. My picture, the logo, and the Title.

```html
<!DOCTYPE html>
<html lang="en">
<head>
<meta charset="utf-8">
<title>Stewardship – Audio CD Sleeve and Disc</title>
<link href="https://fonts.googleapis.com/css2?family=Cinzel:wght@600&family=Lato:wght@400;700&display=swap" rel="stylesheet">
<style>
  :root {
    --backdrop: #5d5e68;
    --gold: #d6c49a;
    --gold-deep: #c8ad76;
    --panel: #1b1c1f;
    --panel-soft: #25272b;
    --label: #e9e9ea;
    --ink: #1a1a1a;
    --text-light: #e4e4e4;
    --disc: #141416;
    --disc-rim: #2b2c30;
    --disc-text: #6e6e72;
    --disc-title: #3c3c40;
  }
  * { margin: 0; padding: 0; box-sizing: border-box; }
  html, body { width: 1200px; height: 757px; overflow: hidden; background: var(--backdrop); }
  .stage { position: relative; width: 1200px; height: 757px; overflow: hidden; }

  .disc { position: absolute; left: 582px; top: 103px; width: 518px; height: 518px; }

  .sleeve {
    position: absolute; left: 232px; top: 83px; width: 569px; height: 548px;
    background: var(--gold);
  }
  .sleeve-panel {
    position: absolute; left: 28px; top: 19px; right: 0; bottom: 19px;
    overflow: hidden;
    background: radial-gradient(ellipse at 75% 40%, var(--panel-soft), var(--panel) 70%);
  }
  .headline {
    position: absolute; left: 34px; top: 55px;
    font-family: "Lato", sans-serif; font-weight: 700; font-size: 18.5px;
    letter-spacing: 1.2px; color: #f2f2f2; line-height: 31px; white-space: nowrap;
  }
  .headline span { display: block; }
  .headline span + span { padding-left: 48px; }
  .intro {
    position: absolute; left: 28px; top: 126px; width: 296px;
    font-family: "Lato", sans-serif; font-size: 11.2px; line-height: 13.2px; color: var(--text-light);
  }
  .bio {
    position: absolute; left: 28px; top: 214px; width: 294px;
    font-family: "Lato", sans-serif; font-size: 9.2px; line-height: 11.5px; color: var(--text-light);
  }
  .intro, .bio { text-indent: 7px; }
  .portrait {
    position: absolute; left: 344px; top: 15px; width: 137px; height: 471px;
    background: linear-gradient(180deg, #33363e 0%, #262931 40%, #1d1f25 100%);
    border-radius: 50px 50px 8px 8px;
  }
  .portrait-caption {
    position: absolute; left: 454px; top: 405px; white-space: nowrap;
    font-family: "Lato", sans-serif; font-size: 9.5px; color: var(--gold);
  }
  .title-label {
    position: absolute; left: 0; top: 345px; width: 250px; height: 92px;
    background: var(--label); border-radius: 0 10px 10px 0;
    display: flex; align-items: center; padding-left: 24px; white-space: nowrap;
    font-family: "Cinzel", serif; font-weight: 600; font-size: 24px;
    letter-spacing: 2px; color: var(--ink);
  }
  .brand {
    position: absolute; left: 11px; top: 453px;
    display: flex; align-items: center; gap: 8px;
  }
  .brand-mark { width: 46px; height: 46px; border-radius: 50%; background: var(--gold); flex: none; }
  .contact {
    font-family: "Lato", sans-serif; font-size: 12.8px; line-height: 15px; color: var(--gold);
    white-space: nowrap;
  }
  .copyright {
    position: absolute; right: 31px; bottom: 6px; white-space: nowrap;
    font-family: "Lato", sans-serif; font-size: 5.6px; color: #c9c9c9;
  }
  .badge {
    position: absolute; right: 10px; bottom: 5px; width: 16px; height: 16px;
    border-radius: 50%; background: #6d78a8;
  }
</style>
</head>
<body>
<main class="stage">

  <svg class="disc" viewBox="0 0 518 518" aria-label="Disc face">
    <defs>
      <path id="arc-subtitle" d="M 482.8 227.5 A 226 226 0 1 0 46.6 336.3"/>
      <path id="arc-title" d="M 441.6 206.6 A 190 190 0 1 0 80.5 324"/>
      <path id="arc-footer" d="M 308.5 491.8 A 238 238 0 1 0 140 52.9"/>
    </defs>
    <circle cx="259" cy="259" r="259" fill="var(--disc-rim)"/>
    <circle cx="259" cy="259" r="253" fill="var(--disc)"/>
    <circle cx="259" cy="259" r="74" fill="none" stroke="#34353a" stroke-width="1.5"/>
    <circle cx="259" cy="259" r="51" fill="var(--gold-deep)"/>
    <circle cx="259" cy="259" r="43" fill="#2a2b2f"/>
    <circle cx="259" cy="259" r="34" fill="#3b3c41"/>
    <text font-family="Lato, sans-serif" font-size="13.5" fill="var(--disc-text)" letter-spacing="0.6">
      <textPath href="#arc-subtitle">Building Lasting Trust Inside Elder Care Homes</textPath>
    </text>
    <text font-family="Cinzel, serif" font-size="32" fill="var(--disc-title)" letter-spacing="3">
      <textPath href="#arc-title">STEWARDSHIP</textPath>
    </text>
    <text font-family="Lato, sans-serif" font-size="7" fill="var(--disc-text)">
      <textPath href="#arc-footer">www.DaleBrannick.com · © 2014 Harbor Lane Group, LLC / All Rights Reserved</textPath>
    </text>
    <path d="M 404 228 H 512 V 289 H 404 a 10 10 0 0 1 -10 -10 V 238 a 10 10 0 0 1 10 -10 Z" fill="var(--label)"/>
    <circle cx="408" cy="259" r="6" fill="var(--gold-deep)"/>
    <text x="419" y="263" font-family="Lato, sans-serif" font-size="10.5" fill="var(--ink)">Dale Brannick</text>
  </svg>

  <section class="sleeve">
    <div class="sleeve-panel">
      <div class="portrait" role="img" aria-label="Portrait photo of Dale Brannick in a dark suit"></div>
      <h1 class="headline"><span>All Businesses Rise</span><span>Or Fall With Leadership</span></h1>
      <p class="intro">This is especially true in the senior living industry. The life of that rise or fall is based on the culture the leader creates. Learn the 3 keys to what leaders know and do. Learn what the importance factor is and how you can put it to work to create and sustain a winning culture that will drive your business and occupancy above the rest.</p>
      <p class="bio">Dale Brannick’s experience in the Senior Living Industry ranges from caregiver to becoming an executive director at the age of 22. He has operated licensed communities from 12 to 250 beds in the assisted living arena. Making lots of mistakes as a young director he has made it his purpose to understand what drives the business and how to create cultures of excellence. He has spent his career transforming troubled communities starting with their culture.</p>
      <p class="portrait-caption">Dale Brannick</p>
      <div class="brand">
        <span class="brand-mark"></span>
        <p class="contact">www.DaleBrannick.com<br>info@DaleBrannick.com</p>
      </div>
      <p class="copyright">© 2014 Harbor Lane Group, LLC / All Rights Reserved</p>
      <span class="badge"></span>
    </div>
    <div class="title-label">STEWARDSHIP</div>
  </section>

</main>
</body>
</html>
```